www.brightlingua.example -- International Language school needs a Wordpress Design

NOTE: This is for a complete WordPress website with coding (Design/develop)

We are a small, private English language school in business for 15 years. Our students come from around the world to study English at our centre in Toronto, Canada. Most of our students are in their 20's and come to study English with us for periods of 1-6 months before returning home to complete their post-secondary education or pursue their careers.

We are looking for a talented web designer to redevelop our sadly outdated website (www.brightlingua.example) to bring a fresh look with vastly increased functionality and web traffic.

Target Market(s)

-20s and 30s; mostly upper-middle class, educated
-from non-English speaking countries, but often have some English background
-looking to improve their English (mostly speaking) skills at our school like ours and experience living in a new country (like exchange students)

Industry/Entity Type

Education

Font styles to use
Sans Serif

Requirements
Must have
• - page listing our programs
- page with our fees and starting dates
- application form
- page showing why BRIGHT (us)?
- page with accommodation options
* responsive design
Nice to have
• examples of other websites in our industry I like:

http://www.maryholt.example/
http://www.tqlearn.example/en
http://en.rpz.example/
http://www.harrowgate-college.example/

```html
<!DOCTYPE html>
<html lang="en">
<head>
<meta charset="utf-8">
<title>BRIGHT — International Language School</title>
<link rel="stylesheet" href="https://fonts.googleapis.com/css2?family=Arimo:ital,wght@0,400;0,700;1,700&family=Cinzel:wght@400&family=Roboto+Condensed:wght@400;700&family=Tinos:wght@400;700&family=Ubuntu:wght@400;500;700&display=swap">
<style>
:root{
  --bar:#2b2b2b;
  --sand:#d3ccc1;
  --stone:#aca59b;
  --accent:#e85a38;
  --accent-text:#e2532f;
  --ink:#222;
  --muted:#85817a;
  --line:#bdb6ab;
  --button:#2a2a2a;
  --white:#fff;
}
*{margin:0;padding:0;box-sizing:border-box}
html,body{width:1200px;height:2557px;overflow:hidden}
body{position:relative;background:var(--sand);font-family:"Ubuntu",sans-serif;color:var(--ink)}
.abs{position:absolute}

/* header */
.site-header{position:absolute;left:0;top:0;width:1200px;height:99px;background:var(--bar)}
.brand{position:absolute;left:26px;top:5px;width:101px;height:87px;background:var(--white);display:flex;align-items:center;justify-content:center;gap:6px}
.brand-mark{width:14px;height:14px;background:var(--accent)}
.brand-name{font-family:"Arimo",sans-serif;font-weight:700;font-size:19px;color:var(--bar)}
.main-nav{position:absolute;right:8px;top:34px;display:flex;gap:6px;font-family:"Tinos",serif;font-size:14.5px;color:var(--white);text-transform:uppercase}
.main-nav a{color:inherit;text-decoration:none;padding:7px 5px;line-height:19px}
.main-nav a.current{background:var(--accent)}

/* offers */
.offers{position:absolute;left:0;top:99px;width:1200px;height:185px;background:var(--sand)}
.offers-title{position:absolute;left:26px;top:62px;font-family:"Arimo",sans-serif;font-weight:700;font-size:25px;line-height:28px;color:#2d2d2d}
.offer{position:absolute;top:27px;width:380px}
.offer-icon{position:absolute;left:0;top:0;width:34px;height:38px}
.offer h3{position:absolute;left:42px;top:14px;font-family:"Roboto Condensed",sans-serif;font-weight:400;font-size:21px;color:#2d2d2d;white-space:nowrap}
.offer h4{position:absolute;left:2px;top:50px;font-size:10.5px;font-weight:700;letter-spacing:.3px;color:#333}
.offer p{position:absolute;left:2px;top:67px;width:360px;font-size:11px;line-height:19px;font-style:italic;color:var(--muted)}
.offer p span{color:var(--accent)}
.offers-divider{position:absolute;left:712px;top:29px;width:1px;height:130px;background:var(--line)}

/* slider */
.slider-band{position:absolute;left:0;top:284px;width:1200px;height:550px;background:var(--stone)}
.slide{position:absolute;left:26px;top:26px;width:1147px;height:500px;background:linear-gradient(100deg,#d8c3ae 0%,#b98f72 30%,#7a5846 55%,#c9a084 80%,#e7d7c6 100%)}
.slide-caption{position:absolute;left:0;width:100%;top:20px;text-align:center;font-family:"Arimo",sans-serif;font-size:13px;color:#222}
.slide-arrow{position:absolute;top:250px;width:40px;height:40px;background:#f5e9c8}
.slide-arrow.prev{left:0}
.slide-arrow.next{right:0}
.slide-tag{position:absolute;left:0;top:380px;width:455px;height:120px;background:var(--accent);color:var(--white);font-family:"Cinzel",serif;padding:20px 0 0 28px}
.slide-tag strong{display:block;font-weight:400;font-size:46px;line-height:46px}
.slide-tag span{display:block;font-size:26px;line-height:32px}

/* welcome */
.welcome{position:absolute;left:0;top:834px;width:1200px;height:274px;background:var(--accent);color:var(--white)}
.welcome h2{position:absolute;left:26px;top:38px;font-family:"Arimo",sans-serif;font-size:27px;font-weight:700}
.welcome .lead{position:absolute;left:26px;top:70px;font-family:"Roboto Condensed",sans-serif;font-size:16px}
.welcome .body{position:absolute;left:26px;top:104px;width:1150px;font-size:11.5px;line-height:21px;color:#f7c8b6}
.welcome ul{position:absolute;left:26px;top:164px;list-style:none;font-size:13px;line-height:21px;color:#fde0a6}
.btn{position:absolute;display:flex;align-items:center;justify-content:center;background:var(--button);color:var(--white);font-family:"Arimo",sans-serif;font-weight:700;font-size:15px;border-radius:3px;box-shadow:0 1px 2px rgba(0,0,0,.4)}

/* features */
.features{position:absolute;left:0;top:1108px;width:1200px;height:492px}
.features-rule{position:absolute;left:0;top:445px;width:1200px;height:1px;background:var(--line)}
.col-divider{position:absolute;top:42px;width:1px;height:450px;background:var(--line)}
.feature{position:absolute;top:52px;width:392px;text-align:center}
.feature-photo{width:154px;height:154px;border-radius:50%;border:4px solid #111;margin:0 auto;background:radial-gradient(circle at 50% 40%,#c9a58b,#6c5648)}
.feature h3{margin-top:29px;font-family:"Tinos",serif;font-weight:700;font-size:28px;letter-spacing:1px;color:var(--accent-text)}
.feature h4{margin-top:1px;font-family:"Arimo",sans-serif;font-weight:400;font-size:24px;color:#333}
.feature p{margin:26px auto 0;width:270px;font-size:12.5px;line-height:21.5px;color:var(--muted)}

.section-rule{position:absolute;left:26px;top:1662px;width:1147px;height:1px;background:var(--line)}

/* programs */
.programs-title{position:absolute;left:26px;top:1714px;font-family:"Arimo",sans-serif;font-weight:700;font-size:21px;line-height:24px;color:#111}
.post{position:absolute;top:1791px;width:328px}
.post-photo{width:328px;height:166px;border:1px solid #777;background:linear-gradient(180deg,#e9e5df,#9a7c6a)}
.post h5{margin-top:25px;font-size:11.5px;font-weight:700;color:#333}
.post-meta{margin-top:17px;display:flex;gap:18px;font-size:11.5px;color:var(--muted);align-items:center}
.post-meta i{display:inline-block;width:12px;height:12px;background:var(--accent);margin-right:6px;vertical-align:-2px;border-radius:2px}
.post p{margin-top:13px;font-size:12px;line-height:22px;color:var(--muted)}

/* faq */
.faq-title{position:absolute;left:811px;top:1708px;font-family:"Arimo",sans-serif;font-weight:700;font-size:27px;line-height:31px;color:#2d2d2d}
.faq-open{position:absolute;left:811px;top:1791px;width:362px}
.faq-q{display:flex;align-items:center;gap:12px;font-size:13.5px;font-weight:500;text-transform:uppercase}
.faq-q svg{flex:none}
.faq-open .faq-q{color:var(--accent-text)}
.faq-open p{margin-top:14px;font-size:12px;line-height:20px;color:var(--muted)}
.faq-item{position:absolute;left:811px;width:362px;border-top:1px solid var(--line);padding-top:19px;color:var(--white)}

/* footer */
.footer-band{position:absolute;left:0;top:2229px;width:1200px;height:8px;background:var(--stone)}
.footer-col{position:absolute;top:2278px;width:263px}
.footer-col h6{font-family:"Arimo",sans-serif;font-style:italic;font-weight:700;font-size:15px;color:#333;padding-bottom:12px;border-bottom:1px solid var(--line)}
.footer-col ul{list-style:none;margin-top:12px;font-family:"Arimo",sans-serif;font-size:10px;font-weight:700;color:#444;text-transform:uppercase}
.footer-col li{height:29.5px}
.footer-col li::before{content:"›";margin-right:7px}
.social{position:absolute;top:2502px;display:flex;gap:6px}
.social span{width:30px;height:30px;background:#8e8e8e;border-radius:2px}
.copyright{position:absolute;left:150px;top:2512px;font-size:10px;color:var(--accent-text)}
</style>
</head>
<body>

<header class="site-header">
  <div class="brand"><span class="brand-mark"></span><span class="brand-name">BRIGHT</span></div>
  <nav class="main-nav">
    <a class="current">Home</a><a>Our School</a><a>Programs</a><a>Fees&amp;Dates</a><a>Accomodation</a><a>After Class Agents</a>
  </nav>
</header>

<section class="offers">
  <h2 class="offers-title">Special Offers<br>of The Week</h2>
  <div class="offer" style="left:318px">
    <svg class="offer-icon" viewBox="0 0 34 38"><rect x="2" y="6" width="22" height="28" rx="3" fill="#e85a38"/><text x="13" y="28" font-family="Arimo" font-weight="700" font-size="20" fill="#fff" text-anchor="middle">$</text></svg>
    <h3>Pellentesque sed Dolor</h3>
    <h4>LOREM IPSUM DOLOR SIT AMET.</h4>
    <p>Conse etuer adipiscing elit, sed diam nonummy nibh euismod tincidunt ut laoreet dolore magn aliquam erat volutpat massa. dolor sit amet, conse etuer adipiscing. <span>›</span></p>
  </div>
  <div class="offers-divider"></div>
  <div class="offer" style="left:810px">
    <svg class="offer-icon" viewBox="0 0 34 38"><circle cx="23" cy="7" r="5" fill="#e85a38"/><rect x="17" y="14" width="12" height="22" fill="#e85a38"/><rect x="2" y="10" width="12" height="6" fill="#e85a38"/><rect x="5" y="16" width="6" height="20" fill="#e85a38"/></svg>
    <h3>Donec sagittis Euismod</h3>
    <h4>LOREM IPSUM DOLOR SIT AMET.</h4>
    <p>Conse etuer adipiscing elit, sed diam nonummy nibh euismod tincidunt ut laoreet dolore magn aliquam erat volutpat massa. dolor sit amet, conse etuer adipiscing. <span>›</span></p>
  </div>
</section>

<section class="slider-band">
  <div class="slide" role="img" aria-label="Group of smiling young students close together">
    <div class="slide-caption">BRIEF INTRO TO SCHOOL</div>
    <div class="slide-arrow prev"><svg width="40" height="40" viewBox="0 0 40 40"><path d="M23 12l-8 8 8 8" stroke="#111" stroke-width="3" fill="none"/></svg></div>
    <div class="slide-arrow next"><svg width="40" height="40" viewBox="0 0 40 40"><path d="M17 12l8 8-8 8" stroke="#111" stroke-width="3" fill="none"/></svg></div>
    <div class="slide-tag"><strong>MAKE FRIENDS</strong><span>FROM AROUN THE WORLD!</span></div>
  </div>
</section>

<section class="welcome">
  <h2>Welcome to Our Site!</h2>
  <p class="lead">Maecenas tristique orci ac sem duis ultricies pharetra magna donec accumsan!</p>
  <p class="body">Lorem ipsum dolor sit amet, consectetuer adipiscing elit. Praesent vestibulum molestie lacus. Aenean nonummy hendrerit mauris. Phasellus porta. Fusce suscipit varius mi. Cum sociis natoque penatibus et magnis dis parturient montes, nascetur ridiculus mus. Nulla dui. Fusce feugiat malesuada odio. Morbi nunc odio, gravida at, cursus nec, luctus a, lorem. Maecenas tristique orci ac sem. Duis ultricies pharetra magna. Donec accumsan malesuada orci.</p>
  <ul>
    <li>* Sed in lacus ut enim adipiscing aliquet ulla venenatis</li>
    <li>* In pede mi, aliquet sit amet, euismod in,auctor ut, ligula dapibus tincidunt metus</li>
    <li>* Praesent justo dolor, lobortis quis, lobortis dignissim, pulvinar ac, lorem</li>
  </ul>
  <a class="btn" style="left:895px;top:198px;width:130px;height:45px">Learn More</a>
  <a class="btn" style="left:1043px;top:198px;width:131px;height:45px">Contact Us</a>
</section>

<section class="features">
  <div class="features-rule"></div>
  <div class="col-divider" style="left:419px"></div>
  <div class="col-divider" style="left:811px"></div>
  <div class="feature" style="left:11px">
    <div class="feature-photo" role="img" aria-label="Students in life jackets on a boat trip"></div>
    <h3>ASK A QUESTION</h3><h4>LIFE</h4>
    <p>Corrupti quos dolores et quas molestias excepturi sint occaecati cupiditate non provident, similique sunt in culpa qui officia deserunt mollitia animi, id est laborum.</p>
  </div>
  <div class="feature" style="left:403px">
    <div class="feature-photo" role="img" aria-label="Group of young women students standing together"></div>
    <h3>GET A QUOTE</h3><h4>FINANCE</h4>
    <p>Corrupti quos dolores et quas molestias excepturi sint occaecati cupiditate non provident, similique sunt in culpa qui officia deserunt mollitia animi, id est laborum.</p>
  </div>
  <div class="feature" style="left:797px">
    <div class="feature-photo" role="img" aria-label="Smiling student outdoors with classmates"></div>
    <h3>APPLY NOW</h3><h4>MOTIVATION</h4>
    <p>Corrupti quos dolores et quas molestias excepturi sint occaecati cupiditate non provident, similique sunt in culpa qui officia deserunt mollitia animi, id est laborum.</p>
  </div>
  <a class="btn" style="left:142px;top:426px;width:132px;height:43px">Read More</a>
  <a class="btn" style="left:536px;top:426px;width:132px;height:43px">Read More</a>
  <a class="btn" style="left:928px;top:426px;width:132px;height:43px">Read More</a>
</section>

<div class="section-rule"></div>

<h2 class="programs-title">ADULT<br>ENGLISH PROGRAMS</h2>
<article class="post" style="left:26px">
  <div class="post-photo" role="img" aria-label="Group of adult students standing in a row"></div>
  <h5>LOREM IPSUM DOLORE EST</h5>
  <div class="post-meta"><span><i></i>by admin</span><span><i></i>comments 0</span></div>
  <p>Lorem ipsum dolor sit amet, consectetur adipisicing elit, sed do eiusmod tempor incididunt ut labore et dolore magna aliqua. Ut enim ad minim...</p>
</article>
<article class="post" style="left:419px">
  <div class="post-photo" role="img" aria-label="Students with books outdoors under trees" style="border:none;background:linear-gradient(180deg,#3d4a2c,#5a4232)"></div>
  <h5>MASSA AS LAORRETUM</h5>
  <div class="post-meta"><span><i></i>by admin</span><span><i></i>comments 0</span></div>
  <p>Lorem ipsum dolor sit amet, consectetur adipisicing elit, sed do eiusmod tempor incididunt ut labore et dolore magna aliqua. Ut enim ad minim...</p>
</article>
<a class="btn" style="left:26px;top:2131px;width:130px;height:43px">View All</a>

<h2 class="faq-title">Frequently Asked<br>Questions</h2>
<div class="faq-open">
  <div class="faq-q"><svg width="18" height="18" viewBox="0 0 18 18"><circle cx="9" cy="9" r="9" fill="#2a2a2a"/><rect x="4" y="8" width="10" height="2" fill="#fff"/></svg>Lorem ipsum dolore</div>
  <p>Phasellus porta. Fusce susct varius mi. Cum sociis natoque penabus et magnis dis parturient montes, nascetur ridicu lus mus. Nulla dui massa dolore sed lorem.</p>
</div>
<div class="faq-item" style="top:1925px"><div class="faq-q"><svg width="18" height="18" viewBox="0 0 18 18"><circle cx="9" cy="9" r="9" fill="#2a2a2a"/><rect x="4" y="8" width="10" height="2" fill="#fff"/><rect x="8" y="4" width="2" height="10" fill="#fff"/></svg>Massa as laoreetum</div></div>
<div class="faq-item" style="top:1985px"><div class="faq-q"><svg width="18" height="18" viewBox="0 0 18 18"><circle cx="9" cy="9" r="9" fill="#2a2a2a"/><rect x="4" y="8" width="10" height="2" fill="#fff"/><rect x="8" y="4" width="2" height="10" fill="#fff"/></svg>Cum sociis ridiculum</div></div>
<div class="faq-item" style="top:2045px"><div class="faq-q"><svg width="18" height="18" viewBox="0 0 18 18"><circle cx="9" cy="9" r="9" fill="#2a2a2a"/><rect x="4" y="8" width="10" height="2" fill="#fff"/><rect x="8" y="4" width="2" height="10" fill="#fff"/></svg>Cum sociis ridiculum</div></div>

<footer>
  <div class="footer-band"></div>
  <div class="footer-col" style="left:26px"><h6>COMPANY</h6><ul><li>Vestibulum iaculis</li><li>Lacinia est</li><li>Proin dictum</li><li>Elementum velit</li><li>Consequat ante</li></ul></div>
  <div class="footer-col" style="left:322px"><h6>OVERVIEW</h6><ul><li>Lorem ipsum dolor</li><li>Sit amet</li><li>Consectetuer</li></ul></div>
  <div class="footer-col" style="left:616px"><h6>FOR CLIENTS</h6><ul><li>Dolor</li><li>Aliquam congue</li><li>Fermentum nisl</li><li>Mauris accumsan</li></ul></div>
  <div class="footer-col" style="left:909px"><h6>ARCHIVE</h6><ul><li>May 2013</li><li>April 2013</li><li>March 2013</li><li>June 2013</li><li>July 2013</li></ul></div>
  <div class="social" style="left:26px"><span></span><span></span><span></span></div>
  <p class="copyright">© 2015 | PRIVACY POLICY</p>
</footer>

</body>
</html>
```